Business card design needed

We need a new business card design to re launch my carpentry business. Could include double sided card with list of services provided.
Kitchens, bathrooms, decks, pergolas, window replacements, timber floor installation, owner builder assistance and general carpentry.
Would like an eye catching card that becons to be read in bright colors that has a logo that could be also used on clothing vehicle sinage etc
Preferably in blues and reds we live near beach so maybe some type of Beecher feel
Target Market(s)
The target market of my business would be mainly individuals requiring professional carpentry services not just a handy man. The renovation market plays a big part of my business
Industry/Entity Type
Carpentry
Contact Information for Business Card
Carpenter & joiner
Rob Pelham
Inverloch
gilda_robbo@tarnmail.com
0439862150
Look and feel
Each slider illustrates characteristics of the customer's brand and the style your logo design should communicate.

```html
<!DOCTYPE html>
<html lang="en">
<head>
<meta charset="utf-8">
<title>Rob Pelham – Carpenter &amp; Joiner business card</title>
<link rel="stylesheet" href="https://fonts.googleapis.com/css2?family=Nunito:wght@800;900&family=Mulish:wght@300;400&display=swap">
<style>
  :root {
    --backdrop: #564d4e;
    --sea: #35c1d8;
    --sand: #f4a572;
    --paper: #ffffff;
    --ink: #1c1c1c;
    --deep: #1f3540;
  }
  * { margin: 0; padding: 0; box-sizing: border-box; }
  html, body { width: 1200px; height: 1000px; overflow: hidden; }
  body {
    background: var(--backdrop);
    position: relative;
    font-family: "Mulish", sans-serif;
  }
  .card {
    position: absolute;
    top: 96px;
    width: 457px;
    height: 790px;
    box-shadow: 3px 4px 6px rgba(0,0,0,0.35);
    text-align: center;
  }
  .card--front { left: 88px; background: var(--sea); }
  .card--back { left: 659px; background: var(--paper); }

  .brand-mark {
    position: absolute;
    left: 0; right: 0;
    display: flex;
    align-items: center;
    justify-content: center;
    gap: 14px;
    font-family: "Nunito", sans-serif;
    font-weight: 800;
  }
  .brand-mark__dot { border-radius: 50%; }
  .card--front .brand-mark { top: 330px; font-size: 34px; color: var(--sand); }
  .card--front .brand-mark__dot { width: 44px; height: 44px; background: var(--sand); }
  .card--back .brand-mark { top: 608px; font-size: 26px; color: var(--sea); }
  .card--back .brand-mark__dot { width: 34px; height: 34px; background: var(--sea); }

  .owner {
    position: absolute;
    top: 392px; left: 0; right: 0;
    color: var(--paper);
    font-family: "Nunito", sans-serif;
    font-weight: 900;
    line-height: 1;
  }
  .owner__first { display: block; font-size: 31px; }
  .owner__last { display: block; font-size: 46px; margin-top: 6px; letter-spacing: 0.5px; text-transform: uppercase; }

  .trade {
    position: absolute;
    top: 538px; left: 86px; right: 91px;
    height: 76px;
    border-left: 3px solid var(--paper);
    border-right: 3px solid var(--paper);
    padding-top: 14px;
  }
  .trade__role { font-size: 23px; color: var(--deep); font-weight: 400; }
  .trade__place { font-size: 15px; color: var(--paper); letter-spacing: 6px; margin-top: 2px; }

  .services {
    position: absolute;
    top: 120px; left: 0; right: 0;
    list-style: none;
    font-size: 29px;
    font-weight: 300;
    line-height: 39px;
  }
  .services li:nth-child(odd) { color: var(--sea); }
  .services li:nth-child(even) { color: var(--sand); }

  .contact {
    position: absolute;
    top: 590px; left: 0; right: 0;
    color: var(--ink);
  }
  .contact__name {
    font-family: "Mulish", sans-serif;
    font-weight: 400;
    font-weight: 700;
    color: var(--sea);
    font-size: 25px;
    margin-bottom: 10px;
  }
  .contact__email, .contact__phone { font-size: 23px; font-weight: 400; line-height: 32px; }
</style>
</head>
<body>
  <section class="card card--front">
    <div class="brand-mark"><span class="brand-mark__dot"></span>Rob Pelham</div>
    <h1 class="owner"><span class="owner__first">Rob</span><span class="owner__last">Pelham</span></h1>
    <div class="trade">
      <p class="trade__role">Carpenter &amp; Joiner</p>
      <p class="trade__place">INVERLOCH</p>
    </div>
  </section>

  <section class="card card--back">
    <ul class="services">
      <li>kitchens</li>
      <li>bathrooms</li>
      <li>decks</li>
      <li>pergolas</li>
      <li>window replacements</li>
      <li>timber floor installation</li>
      <li>owner builder assistance</li>
      <li>general carpentry</li>
    </ul>
    <div class="brand-mark"><span class="brand-mark__dot"></span>Rob Pelham</div>
    <div class="contact" style="top:690px">
      <p class="contact__email">gilda_robbo@tarnmail.com</p>
      <p class="contact__phone">Tel: 0439862150</p>
    </div>
  </section>
</body>
</html>
```